Retro game shop business card design

We need a card designed both front and back. we already have a logo. The business name is called Brisk Copper Atlas and we work on customizing and modifying old velmora zuma tabs. Our website is briskcopperatlas.com

our business cards are often shown in glintly posts ans should be designed so that you can easy identify and see in am image. @briskcopperatlas.

Target Market(s)

men 13-40

Contact Information for Business Card

should have logo, wesbite, and if possible some artwork related to zuma tab mods

Font styles to use
Sans Serif

Colors

Designer to choose colors to be used in the design.

Requirements
Must have
• logo, website url www.briskcopperatlas.com, hastag #zumatabmods, email, support@briskcopperatlas.com. zuma tab imagry only (illustration preffered)
Nice to have
• illustrations, graphic design with zuma tab mods (see glintly #zumatabmods)
Should not have
• childlike depictions of zumatabs, kids, anything unrelated to zuma tab mods, no hands, no bertil, no pixel art

```html
<!DOCTYPE html>
<html lang="en">
<head>
<meta charset="utf-8">
<title>Brisk Copper Atlas – Business Card</title>
<link href="https://fonts.googleapis.com/css2?family=Arimo:wght@400;700&display=swap" rel="stylesheet">
<style>
  :root {
    --backdrop: #b9b9b9;
    --card-white: #ffffff;
    --ink: #231f20;
    --logo-light: #d9dcdb;
    --shadow: rgba(0, 0, 0, 0.35);
  }
  * { margin: 0; padding: 0; box-sizing: border-box; }
  html, body {
    width: 1200px;
    height: 802px;
    overflow: hidden;
    background: var(--backdrop);
    font-family: "Arimo", Arial, sans-serif;
  }
  .card {
    position: absolute;
    top: 274px;
    width: 442px;
    height: 264px;
    box-shadow: 2px 4px 8px var(--shadow);
    overflow: hidden;
  }
  .card--front { left: 136px; background: var(--card-white); }
  .card--back { left: 624px; background: var(--ink); }

  .front-band {
    position: absolute;
    left: 0; top: 0;
    width: 442px; height: 264px;
  }
  .brand-name {
    position: absolute;
    font-weight: 700;
    line-height: 1.02;
    letter-spacing: 0.5px;
    text-transform: uppercase;
  }
  .card--front .brand-name {
    right: 28px;
    top: 40px;
    font-size: 30px;
    color: var(--ink);
    text-align: right;
  }
  .card--back .brand-name {
    left: 0; right: 0;
    top: 96px;
    font-size: 34px;
    color: var(--logo-light);
    text-align: center;
  }
  .rule {
    position: absolute;
    left: 54px;
    height: 2.5px;
    background: var(--ink);
  }
  .rule--top { top: 124px; width: 184px; }
  .rule--bottom { top: 224px; width: 358px; }

  .contact-list {
    position: absolute;
    left: 57px;
    top: 141px;
    list-style: none;
  }
  .contact-item {
    font-size: 12.5px;
    color: var(--ink);
    height: 24px;
    line-height: 18px;
  }
  .contact-icons {
    position: absolute;
    left: 16px;
    top: 137px;
    width: 26px;
    height: 74px;
  }
</style>
</head>
<body>
  <section class="card card--front" aria-label="Card front">
    <svg class="front-band" viewBox="0 0 442 264" aria-hidden="true">
      <polygon points="0,79 50,134 50,227 81,264 0,264" fill="var(--ink)"/>
    </svg>

    <div class="brand-name">Brisk Copper<br>Atlas</div>

    <div class="rule rule--top"></div>

    <svg class="contact-icons" viewBox="0 0 26 74" aria-hidden="true">
      <g fill="none" stroke="#fff" stroke-width="1.2">
        <circle cx="12" cy="12" r="10"/>
        <circle cx="12" cy="36" r="10"/>
        <circle cx="12" cy="36" r="5.5"/>
        <path d="M6.5 36h11M12 30.5c-2.5 3-2.5 8 0 11M12 30.5c2.5 3 2.5 8 0 11"/>
        <circle cx="12" cy="60" r="10"/>
      </g>
      <rect x="7" y="56.5" width="10" height="7" rx="1" fill="#fff"/>
      <path d="M7.3 57l4.7 3.6 4.7-3.6" fill="none" stroke="var(--ink)" stroke-width="1"/>
    </svg>

    <ul class="contact-list">
      <li class="contact-item">#zumatabmods</li>
      <li class="contact-item">www.briskcopperatlas.com</li>
      <li class="contact-item">support@briskcopperatlas.com</li>
    </ul>

    <div class="rule rule--bottom"></div>
  </section>

  <section class="card card--back" aria-label="Card back">
    <div class="brand-name">Brisk Copper<br>Atlas</div>
  </section>
</body>
</html>
```